TVRB web site redesign

Meridale Linkworks Provisioning service (TVRB) is a diverse technology company specialising in design and installation of fibre optics, network convergence and building services, for commercial clients in Australia, we required a new design of our website to attract new clients, generate sales leads, and provide information about our services to the market. The site and should have a new technology look and feel and be designed in word press. our branding colour is blue.

Target Market(s)

New developments, Construction organisations, Commercial end users, IT managers, Consultants.

Industry/Entity Type

It Company

Number of Pages Required

5+ page

Font styles to use
Sans Serif

Colors
0292cd
3176b5

Requirements
Must have
• key pages.
• Home page with some sizzle, automated pictures running through, I like the look of this competitor website http://www.lumacrest.com.au/ good clean menus and easy to navigate.
• Services page our key services are Fibre optics, Security, Building services,Electrical. I would like the same page layout (Design) for all our services, with a find out more link on each page, manly picture driven with text around our key messaging.
• About us page with space for company profile and directors pictures, bio and contact information.
• Certifications / Accreditations page with have over 20 certifications on different products from suppliers, and a number of licences from governing bodies.
• Current and past projects page with case studies and customer outcomes
• Contact us page with options around what services they require more information on, please keep in mind the site is around generating sales Leeds and being seen as an industry expert.
Nice to have
• RSS feeds, Linked in link, to be placed within the design, Consistent TVRB branding,Same colour blue as our logo Document library for education information, white papers, presentations etc,
• a new technology look and feel, mobile friendly.
Should not have
• boring layout, move away from our cuurent website http://www.tvrbgroup.com.au/
• no e eCommerce store required.

```html
<!DOCTYPE html>
<html lang="en">
<head>
<meta charset="utf-8">
<title>TVRB — Home</title>
<link href="https://fonts.googleapis.com/css2?family=Raleway:wght@400;500;600;700&family=Roboto+Condensed:wght@300;400&display=swap" rel="stylesheet">
<style>
:root{
  --brand:#0292cd;
  --brand-dark:#3176b5;
  --ink:#333333;
  --muted:#555555;
  --nav:#545454;
  --line:#e2e2e2;
  --footer:#3b3b3b;
  --white:#ffffff;
}
*{box-sizing:border-box;margin:0;padding:0}
html,body{width:837px;height:1200px;overflow:hidden;background:var(--white)}
body{position:relative;font-family:"Raleway",Arial,sans-serif;color:var(--ink)}
.abs{position:absolute}

/* header */
.brand{left:91px;top:18px;display:flex;align-items:center;gap:8px}
.brand-mark{width:30px;height:30px;background:var(--brand)}
.brand-name{font-size:30px;font-weight:700;color:var(--brand);letter-spacing:1px;line-height:1}
.brand-sub{left:91px;top:54px;font-size:5px;font-weight:600;color:var(--brand);text-transform:uppercase;letter-spacing:.1px}
.follow{left:641px;top:17px;font-size:11px;color:#888}
.social{left:642px;top:38px;display:flex;gap:4px}
.social span{width:22px;height:22px;border-radius:50%;display:block}
.s1{background:#1b5fa8}.s2{background:#1e9ad6}.s3{background:#f39a1e}.s4{background:#c9392b}

/* nav */
.nav{left:0;top:80px;width:837px;height:40px;background:var(--nav)}
.nav a{position:absolute;top:0;height:40px;line-height:42px;font-size:9.5px;font-weight:500;color:var(--white);text-decoration:none;letter-spacing:.2px}
.nav a.active{background:var(--brand);width:78px;left:90px;text-align:center}
.caret{display:inline-block;margin-left:9px;border:3.5px solid transparent;border-top:4px solid #fff;vertical-align:-1px}

/* hero */
.hero{left:0;top:120px;width:837px;height:310px;background:#000}
.hero-visual{left:0;top:0;width:445px;height:290px;background:radial-gradient(ellipse at 25% 40%,#1fa3c8 0%,#0d6d8c 30%,#06303e 58%,#000 78%)}
.hero-copy{left:484px;top:92px;width:260px;font-family:"Roboto Condensed",Arial,sans-serif;font-weight:300;color:var(--white);line-height:1}
.hero-copy .l{position:absolute;white-space:nowrap}
.hero-copy .b{color:var(--brand)}
.arrow{top:145px}

/* sections */
.h2{left:0;width:837px;text-align:center;font-size:22px;font-weight:400;color:var(--ink)}
.h2 strong{font-weight:600}
.h2 .b{color:var(--brand-dark)}
.intro{left:100px;top:510px;width:637px;text-align:center;font-size:9.4px;line-height:17.5px;color:var(--muted)}
.btn{left:379px;top:575px;width:82px;height:26px;background:var(--brand);color:var(--white);font-size:9.5px;font-weight:500;text-align:center;line-height:27px}
.rule{left:91px;width:655px;height:1px;background:var(--line)}
.pager{left:725px}

.card{width:201px}
.card-photo{width:201px;height:115px;border:3px solid #eee}
.p1{background:linear-gradient(135deg,#5d5248,#2d2a2a 55%,#7a6a55)}
.p2{background:radial-gradient(circle at 25% 45%,#5cc05c 0 12%,#e6ebea 24%,#cfd6d6 70%)}
.p3{background:linear-gradient(90deg,#c7c2a8,#6e7478 35%,#e8eaec 70%,#2a2c30)}
.card-title{margin-top:17px;text-align:center;font-size:11px;font-weight:500;color:var(--brand-dark);text-transform:uppercase}
.card-text{margin-top:5px;text-align:center;font-size:9.2px;line-height:13px;color:var(--muted)}

.post{top:982px;width:315px;height:110px;border:1px solid var(--line)}
.avatar{left:14px;top:18px;width:36px;height:36px;border-radius:50%}
.a1{background:#5a4740}.a2{background:#8c8178}
.post-title{left:62px;top:17px;font-size:14.5px;color:var(--brand-dark)}
.post-text{left:62px;top:37px;width:245px;font-size:9.2px;line-height:17px;color:var(--muted)}
.post-meta{left:62px;top:80px;display:flex;gap:9px;font-size:8px;color:var(--ink);align-items:center}
.post-meta span{display:flex;align-items:center;gap:4px}

.footer{left:0;top:1133px;width:837px;height:67px;background:var(--footer)}
.copy{left:93px;top:32px;font-size:9px;color:#eee}
.totop{left:728px;top:27px}
</style>
</head>
<body>

<header>
  <div class="abs brand"><span class="brand-mark"></span><span class="brand-name">TVRB</span></div>
  <div class="abs brand-sub">Meridale Linkworks Provisioning service</div>
  <div class="abs follow">Follow Us</div>
  <div class="abs social"><span class="s1"></span><span class="s2"></span><span class="s3"></span><span class="s4"></span></div>
</header>

<nav class="abs nav">
  <a class="active" href="#">HOME</a>
  <a href="#" style="left:199px">SERVICES <i class="caret"></i></a>
  <a href="#" style="left:300px">ABOUT US</a>
  <a href="#" style="left:392px">CERTIFICATIONS</a>
  <a href="#" style="left:509px">CURRENT / PAST PROJECTS</a>
  <a href="#" style="left:679px">CONTACT US</a>
</nav>

<section class="abs hero">
  <div class="abs hero-visual" role="img" aria-label="Glowing blue fibre optic strands fanning out on black"></div>
  <svg class="abs arrow" style="left:44px" width="14" height="20" viewBox="0 0 14 20"><path d="M11 2 3 10l8 8" fill="none" stroke="#fff" stroke-width="3"/></svg>
  <svg class="abs arrow" style="left:781px" width="14" height="20" viewBox="0 0 14 20"><path d="M3 2l8 8-8 8" fill="none" stroke="#fff" stroke-width="3"/></svg>
  <div class="abs hero-copy">
    <div class="l b" style="left:1px;top:0;font-size:25px">TVRB <span style="font-size:16px">has an</span></div>
    <div class="l" style="left:55px;top:30px;font-size:24px">Exceptional Team</div>
    <div class="l" style="left:3px;top:59px;font-size:24px"><span class="b" style="font-size:17px">of very</span> Experienced <span class="b" style="font-size:17px">and</span></div>
    <div class="l" style="left:3px;top:88px;font-size:24px">well-qualified management</div>
    <div class="l" style="left:88px;top:116px;font-size:24px"><span class="b" style="font-size:17px">and</span> Tradespersons</div>
  </div>
</section>

<main>
  <h1 class="abs h2" style="top:468px">Welcome to Our Site <strong>Mainpage</strong></h1>
  <p class="abs intro">Lorem ipsum dolor sit amet, consectetur adipiscing elit, sed do eiusmod tempor incididunt ut labore et dolore magna aliqua. Ut enim ad minim veniam, quis nostrud exercitation ullamco laboris nisi ut aliquip ex ea commodo consequat. Duis aute irure dolor in reprehenderit in voluptate velit esse cillum dolore eu fugiat nulla pariatur epteur sint occaecat cupidatat non.</p>
  <div class="abs btn">Read More</div>
  <div class="abs rule" style="top:628px"></div>

  <h2 class="abs h2" style="top:657px">Our <strong>Services</strong></h2>
  <svg class="abs pager" style="top:665px" width="22" height="14" viewBox="0 0 22 14"><path d="M8 2 3 7l5 5" fill="none" stroke="#444" stroke-width="2.4"/><path d="M15 2l5 5-5 5" fill="none" stroke="#bbb" stroke-width="2.4"/></svg>

  <div class="abs card" style="left:91px;top:700px">
    <div class="card-photo p1" role="img" aria-label="Fibre optic splicing machine with coloured cables"></div>
    <div class="card-title">Fibre Optics</div>
    <div class="card-text">Duis aute irure dolor in reprehenderit<br>in voluptate velit esse cillu.</div>
  </div>
  <div class="abs card" style="left:318px;top:700px">
    <div class="card-photo p2" role="img" aria-label="Green unlocked padlock under a magnifier on a digital background"></div>
    <div class="card-title">Security</div>
    <div class="card-text">Duis aute irure dolor in reprehenderit<br>in voluptate velit esse cillu.</div>
  </div>
  <div class="abs card" style="left:544px;top:700px">
    <div class="card-photo p3" role="img" aria-label="Technician with a laptop beside server racks"></div>
    <div class="card-title">Building Services</div>
    <div class="card-text">Duis aute irure dolor in reprehenderit<br>in voluptate velit esse cillu.</div>
  </div>

  <div class="abs rule" style="top:912px"></div>

  <h2 class="abs h2" style="top:939px"><strong>Our <span class="b">Blog</span></strong> Post</h2>
  <svg class="abs pager" style="top:945px" width="22" height="14" viewBox="0 0 22 14"><path d="M8 2 3 7l5 5" fill="none" stroke="#444" stroke-width="2.4"/><path d="M15 2l5 5-5 5" fill="none" stroke="#bbb" stroke-width="2.4"/></svg>

  <article class="abs post" style="left:91px">
    <div class="abs avatar a1" role="img" aria-label="Author portrait"></div>
    <div class="abs post-title">Duis aute irure dolor</div>
    <div class="abs post-text">reprehenderit in voluptate velit esse cillum dolore eu fugiat nulla pariatur epteur sint occaec.</div>
    <div class="abs post-meta">
      <span><svg width="8" height="8" viewBox="0 0 8 8"><rect x=".5" y="1.5" width="7" height="6" fill="none" stroke="#555"/><path d="M.5 3.5h7" stroke="#555"/></svg>March 14, 2014</span>
      <span><svg width="8" height="8" viewBox="0 0 8 8"><circle cx="4" cy="4" r="3.4" fill="none" stroke="#555"/><path d="M4 2v2h1.6" fill="none" stroke="#555"/></svg>8:28 PM</span>
    </div>
  </article>
  <article class="abs post" style="left:430px">
    <div class="abs avatar a2" role="img" aria-label="Author portrait"></div>
    <div class="abs post-title">Voluptate velit esse</div>
    <div class="abs post-text">reprehenderit in voluptate velit esse cillum dolore eu fugiat nulla pariatur epteur sint occaec.</div>
    <div class="abs post-meta">
      <span><svg width="8" height="8" viewBox="0 0 8 8"><rect x=".5" y="1.5" width="7" height="6" fill="none" stroke="#555"/><path d="M.5 3.5h7" stroke="#555"/></svg>March 14, 2014</span>
      <span><svg width="8" height="8" viewBox="0 0 8 8"><circle cx="4" cy="4" r="3.4" fill="none" stroke="#555"/><path d="M4 2v2h1.6" fill="none" stroke="#555"/></svg>8:28 PM</span>
    </div>
  </article>
</main>

<footer class="abs footer">
  <div class="abs copy">Copyright ©2014. Yoursite. All Right Reserved</div>
  <svg class="abs totop" width="19" height="19" viewBox="0 0 19 19"><circle cx="9.5" cy="9.5" r="9.5" fill="#fff"/><path d="M5.5 11.5l4-4 4 4" fill="none" stroke="#3b3b3b" stroke-width="2.4"/></svg>
</footer>

</body>
</html>
```